UI Graphics Design For Web Based Home Control

Hi,
Our company Kelvo Systems is looking for user interface graphics in form of *.psd for home control user interface for a real system which can be used on mobile and PC/MAC.
In Ideal solution, the same interface should be used on mobile, tablets, computers. It changes only to fit the size of the screen. The bigger the screen, the more options you have visible on same view. The user should get familiar interface logic with every device.
The design should have at least the following views covered:
1. Lights view
- List of rooms and lamps
- You can see the status and you can switch it on/off
2. Login view
- Logo (company logo attached)
- Username field
- Password field
3. Dashboard view
- Indicating and choosing home/not home
- Can go to lights view
- Can go to settings view
- Notification list
4. Settings view
- View and edit users
- View and edit lights
Show us your view of ideal home control UI :)
Updates
Time of the project extended by 10 days to receive more designs. If someone sees that the reward should be increased, please also provide the amount expected with the first design. We are willing to increase the amount paid if we see a good design.
Reason: We expect to receive more designs. We are willing to increase the reward if we see good and acceptable designs. Please provide the amount expected with the first design. Project will end with full designs available.
We added our input as an attachment how we see the UI logic. Please have a look into the file.
Reason: We are seeing some good designs. We increased the budget. We are still not where we expect.
Industry/Entity Type
It Company
Look and feel
Each slider illustrates characteristics of the customer's brand and the style your logo design should communicate.

```html
<!DOCTYPE html>
<html lang="en">
<head>
<meta charset="utf-8">
<title>My Dashboard – Kelvo Systems</title>
<link rel="stylesheet" href="https://fonts.googleapis.com/css2?family=Source+Sans+3:wght@400;700&display=swap">
<style>
  :root {
    --bg: #161616;
    --bar-top: #2a2a2c;
    --bar-bottom: #1b1b1d;
    --bar-line: #3a3a3e;
    --divider: #3c3c40;
    --glow-core: #4a4f6e;
    --glow-blue: #1c1e6a;
    --text: #ffffff;
    --brand-text: #646a80;
    --house-wall: #f3ead6;
    --house-roof: #4a3a30;
    --house-door: #c8551e;
    --house-window: #a83020;
    --bulb-glass: #e8ecef;
    --bulb-base: #9a9ea3;
    --gear: #b9bcc0;
    --gear-dark: #6e7277;
    --warn: #f4f000;
    --warn-edge: #111111;
    --badge: #b4141c;
  }
  * { margin: 0; padding: 0; box-sizing: border-box; }
  html, body { width: 1200px; height: 750px; overflow: hidden; background: var(--bg); }
  body { font-family: "Source Sans 3", "Myriad Pro", sans-serif; color: var(--text); }

  .dashboard {
    position: relative;
    width: 1200px;
    height: 750px;
    background:
      radial-gradient(ellipse 360px 280px at 600px 150px, var(--glow-core) 0%, rgba(40,44,110,0.55) 45%, rgba(22,22,22,0) 100%),
      radial-gradient(ellipse 520px 330px at 600px 230px, rgba(28,30,106,0.85) 0%, rgba(22,22,40,0.3) 70%, rgba(22,22,22,0) 100%),
      var(--bg);
  }

  .top-bar {
    position: absolute; inset: 0 0 auto 0; height: 68px;
    background: linear-gradient(var(--bar-top), var(--bar-bottom));
    border-bottom: 1px solid var(--bar-line);
    font-weight: 700; font-size: 27px; letter-spacing: -0.2px;
    text-shadow: 0 1px 2px rgba(0,0,0,0.7);
  }
  .top-bar span { position: absolute; top: 16px; line-height: 36px; }
  .top-bar .presence { left: 61px; }
  .top-bar .title { left: 0; right: 0; text-align: center; }
  .top-bar .temperature { left: 906px; }
  .top-bar .temperature sup { font-size: 20px; position: relative; top: -4px; margin-right: 2px; }
  .top-bar .clock { left: 1018px; }
  .top-bar .divider { position: absolute; top: 18px; width: 1px; height: 34px; background: var(--divider); }

  .brand-name {
    position: absolute; left: 0; right: 0; top: 346px; text-align: center;
    font-size: 34px; font-weight: 400; letter-spacing: 2px; color: var(--brand-text);
  }

  .tile { position: absolute; width: 200px; text-align: center; }
  .tile svg { display: block; margin: 0 auto; overflow: visible; }
  .tile-label {
    display: block; font-weight: 700; font-size: 23px; line-height: 28px;
    text-shadow: 0 2px 3px rgba(0,0,0,0.8);
  }
  .tile-home { left: 500px; top: 130px; }
  .tile-home .tile-label { margin-top: 4px; }
  .tile-lights { left: 163px; top: 320px; }
  .tile-lights .tile-label { margin-top: 0; }
  .tile-settings { left: 815px; top: 320px; }
  .tile-settings .tile-label { margin-top: 4px; }
  .tile-notifications { left: 500px; top: 512px; }
  .tile-notifications .tile-label { margin-top: 4px; }
</style>
</head>
<body>
<main class="dashboard">
  <header class="top-bar">
    <span class="presence">At Home</span>
    <i class="divider" style="left:205px"></i>
    <span class="title">My Dashboard</span>
    <i class="divider" style="left:875px"></i>
    <span class="temperature">80<sup>°</sup>F</span>
    <i class="divider" style="left:988px"></i>
    <span class="clock">12:00 am</span>
  </header>

  <div class="brand-name">Kelvo Systems</div>

  <a class="tile tile-home">
    <svg width="80" height="82" viewBox="0 0 80 82" aria-hidden="true">
      <rect x="56" y="8" width="8" height="18" fill="var(--house-roof)"/>
      <polygon points="8,38 40,6 72,38 72,80 8,80" fill="var(--house-wall)"/>
      <polyline points="3,42 40,4 77,42" fill="none" stroke="var(--house-roof)" stroke-width="7" stroke-linejoin="round"/>
      <rect x="26" y="24" width="14" height="13" fill="#dfe6ea" stroke="var(--house-roof)" stroke-width="2"/>
      <rect x="21" y="24" width="5" height="13" fill="var(--house-window)"/>
      <rect x="40" y="24" width="5" height="13" fill="var(--house-window)"/>
      <rect x="31" y="46" width="17" height="33" fill="var(--house-door)" stroke="#7a3010" stroke-width="1.5"/>
    </svg>
    <span class="tile-label">At Home</span>
  </a>

  <a class="tile tile-lights">
    <svg width="56" height="86" viewBox="0 0 56 86" aria-hidden="true">
      <path d="M28 2 C12 2 3 14 3 27 C3 40 14 46 16 60 L40 60 C42 46 53 40 53 27 C53 14 44 2 28 2 Z" fill="var(--bulb-glass)" opacity="0.9"/>
      <path d="M22 58 L24 36 L28 44 L32 36 L34 58" fill="none" stroke="#7d8288" stroke-width="1.5"/>
      <rect x="16" y="60" width="24" height="16" rx="3" fill="var(--bulb-base)"/>
      <path d="M16 64 H40 M16 68 H40 M16 72 H40" stroke="#6a6e73" stroke-width="1.5"/>
      <path d="M22 76 H34 L30 84 H26 Z" fill="#55595e"/>
    </svg>
    <span class="tile-label">Lights</span>
  </a>

  <a class="tile tile-settings">
    <svg width="96" height="84" viewBox="0 0 96 84" aria-hidden="true">
      <g fill="var(--gear-dark)">
        <circle cx="24" cy="22" r="16"/>
        <g stroke="var(--gear-dark)" stroke-width="7">
          <path d="M24 2 V42 M4 22 H44 M10 8 L38 36 M38 8 L10 36"/>
        </g>
      </g>
      <circle cx="24" cy="22" r="6" fill="#1a1a2a"/>
      <g fill="var(--gear)">
        <circle cx="60" cy="50" r="24"/>
        <g stroke="var(--gear)" stroke-width="10">
          <path d="M60 20 V80 M30 50 H90 M39 29 L81 71 M81 29 L39 71"/>
        </g>
      </g>
      <circle cx="60" cy="50" r="10" fill="#1a1a2a"/>
    </svg>
    <span class="tile-label">Settings</span>
  </a>

  <a class="tile tile-notifications">
    <svg width="90" height="72" viewBox="0 0 90 72" aria-hidden="true">
      <polygon points="45,3 87,70 3,70" fill="var(--warn)" stroke="var(--warn-edge)" stroke-width="4" stroke-linejoin="round"/>
      <path d="M41 26 H49 L47 52 H43 Z" fill="var(--warn-edge)"/>
      <circle cx="45" cy="60" r="4.5" fill="var(--warn-edge)"/>
      <circle cx="100" cy="30" r="14" fill="var(--badge)" stroke="#ffffff" stroke-opacity="0.2" stroke-width="1"/>
      <text x="100" y="38" text-anchor="middle" font-family="Source Sans 3, sans-serif" font-weight="700" font-size="21" fill="#ffffff">2</text>
    </svg>
    <span class="tile-label">Notifiations</span>
  </a>
</main>
</body>
</html>
```